Stationery Set for new venture capital firm

We need a new set of stationery including letterhead, business cards, envelopes, with compliment slips for our new startup venture capital firm known as Halvorn.
We make alternative investments globally and hope to have a worldwide network of offices later.

The stationery should be elegant and not too fussy with the use of too many colors.

Venture Capital

```html
<!DOCTYPE html>
<html lang="en">
<head>
<meta charset="utf-8">
<title>Halvorn — Stationery Set</title>
<link rel="stylesheet" href="https://fonts.googleapis.com/css2?family=Open+Sans:wght@400;600&family=Arimo&family=Tinos&display=swap">
<style>
  :root {
    --bg: #c6c7c9;
    --paper: #ffffff;
    --brand-blue: #0a9ade;
    --brand-grey: #6d6e70;
    --ink: #1a1a1a;
    --muted: #8a8a8a;
    --rule: #bfbfbf;
  }
  * { box-sizing: border-box; margin: 0; padding: 0; }
  html, body { width: 1200px; height: 1200px; overflow: hidden; }
  body {
    background: var(--bg);
    position: relative;
    font-family: "Open Sans", Arial, sans-serif;
    color: var(--ink);
  }

  /* Brand wordmark */
  .wordmark { display: flex; align-items: center; gap: 8px; }
  .wordmark__dot { border-radius: 50%; background: var(--brand-blue); flex: none; }
  .wordmark__name {
    font-family: "Open Sans", Arial, sans-serif;
    font-weight: 600;
    color: var(--brand-grey);
    letter-spacing: 0.01em;
    line-height: 1;
  }

  /* Business card */
  .business-card {
    position: absolute; left: 80px; top: 70px;
    width: 390px; height: 225px;
    background: var(--paper);
  }
  .business-card .wordmark { position: absolute; left: 30px; top: 40px; }
  .business-card .wordmark__dot { width: 20px; height: 20px; }
  .business-card .wordmark__name { font-size: 26px; }
  .business-card__person { position: absolute; left: 152px; top: 108px; }
  .business-card__name { font-size: 18px; letter-spacing: 0.04em; font-weight: 400; }
  .business-card__title { font-size: 12px; color: var(--muted); margin-top: 1px; }
  .business-card__contact {
    margin-top: 12px; font-size: 9.5px; line-height: 1.45;
    color: var(--muted); letter-spacing: 0.04em;
  }

  /* Letterhead */
  .letterhead {
    position: absolute; left: 520px; top: 70px;
    width: 620px; height: 877px;
    background: var(--paper);
    font-family: "Arimo", Arial, sans-serif;
    font-size: 12px; line-height: 1.4;
  }
  .letterhead .wordmark { position: absolute; left: 78px; top: 52px; }
  .letterhead .wordmark__dot { width: 20px; height: 20px; }
  .letterhead .wordmark__name { font-size: 26px; }
  .letter { position: absolute; left: 78px; top: 185px; width: 470px; }
  .letter__recipient, .letter__date { margin-bottom: 28px; }
  .letter__salutation { margin-top: 36px; margin-bottom: 14px; }
  .letter__body p { margin-bottom: 14px; }
  .letter__signoff {
    font-family: "Tinos", "Times New Roman", serif;
    font-size: 12px; line-height: 1.35; margin-top: 30px;
  }
  .letter__signoff .signature-space { height: 38px; }
  .letter__cc { margin-top: 24px; }
  .letter__cc span { display: block; padding-left: 18px; }

  /* Envelope */
  .envelope {
    position: absolute; left: 50px; top: 340px;
    width: 440px; height: 210px;
    background: var(--paper);
  }
  .envelope .wordmark { position: absolute; left: 28px; top: 46px; }
  .envelope .wordmark__dot { width: 16px; height: 16px; }
  .envelope .wordmark__name { font-size: 21px; }
  .envelope__window {
    position: absolute; left: 22px; top: 118px;
    width: 155px; height: 50px;
    border: 1.5px solid var(--rule); border-radius: 7px;
  }
  .envelope__sender {
    position: absolute; left: 262px; top: 132px;
    font-size: 7.5px; line-height: 1.45; color: var(--muted); letter-spacing: 0.04em;
  }
  .envelope__sender-name { font-size: 10px; letter-spacing: 0.06em; margin-top: 5px; color: #555; }

  /* Disc label */
  .disc { position: absolute; left: 60px; top: 620px; width: 420px; height: 420px; }
</style>
</head>
<body>

  <section class="business-card" aria-label="Business card">
    <div class="wordmark"><span class="wordmark__dot"></span><span class="wordmark__name">Halvorn</span></div>
    <div class="business-card__person">
      <div class="business-card__name">TEODOR VANSK</div>
      <div class="business-card__title">Managing Director</div>
      <div class="business-card__contact">
        Northgate, Vale Region, 14 Quay Lane<br>
        ph:&nbsp; 555-204-3187; mob: 000 316 2950<br>
        Fax: 555-204-3190
      </div>
    </div>
  </section>

  <section class="letterhead" aria-label="Letterhead">
    <div class="wordmark"><span class="wordmark__dot"></span><span class="wordmark__name">Halvorn</span></div>
    <div class="letter">
      <div class="letter__recipient">
        Domnul Numele Destinatarului,<br>
        Adresa Destinatarului<br>
        Oras, Judet Cod postal
      </div>
      <div class="letter__date">Iasi, Ziua Luna, Anul</div>
      <div class="letter__salutation">Domnului Numele Destinatarului,</div>
      <div class="letter__body">
        <p>Lorem ipsum dolor sit amet, consectetuer adipiscing elit, sed diam nonummy nibh euismod tincidunt ut laoreet dolore magna aliquam erat volutpat. Ut wisi enim ad minim veniam, quis nostrud exerci tation</p>
        <p>ullamcorper suscipit lobortis nisl ut aliquip ex ea commodo consequat. Duis autem vel eum iriure dolor in hendrerit in vulputate velit esse molestie consequat.</p>
        <p>Vel illum dolore eu feugiat nulla facilisis at vero eros et accumsan et iusto odio dignissim qui blandit praesent luptatum zzril delenit augue duis dolore te feugait nulla facilisi.</p>
      </div>
      <div class="letter__signoff">
        Sincerely,
        <div class="signature-space"></div>
        Lucian Moravec<br>
        Deputy Assistant Director
        <div class="letter__cc">Cc: P. Dalvik<span>A. Ressel</span></div>
      </div>
    </div>
  </section>

  <section class="envelope" aria-label="Envelope">
    <div class="wordmark"><span class="wordmark__dot"></span><span class="wordmark__name">Halvorn</span></div>
    <div class="envelope__window"></div>
    <div class="envelope__sender">
      Northgate, Vale Region, 14 Quay Lane<br>
      ph:&nbsp; 555-204-3187; mob: 000 316 2950<br>
      Fax: 555-204-3190
      <div class="envelope__sender-name">TEODOR VANSK</div>
    </div>
  </section>

  <svg class="disc" viewBox="0 0 420 420" aria-label="Disc label">
    <defs>
      <clipPath id="disc-shape"><circle cx="210" cy="210" r="208"/></clipPath>
    </defs>
    <g clip-path="url(#disc-shape)">
      <rect x="0" y="0" width="420" height="420" fill="#ffffff"/>
      <rect x="0" y="0" width="210" height="420" fill="var(--brand-blue)"/>
    </g>
    <circle cx="210" cy="210" r="207" fill="none" stroke="#d0d0d0" stroke-width="2"/>
    <circle cx="210" cy="210" r="68" fill="#ffffff" stroke="#9a9a9a" stroke-width="1.5"/>
    <circle cx="210" cy="210" r="56" fill="none" stroke="#9a9a9a" stroke-width="1.2"/>
    <circle cx="210" cy="210" r="24" fill="#c6c7c9" stroke="#9a9a9a" stroke-width="1.2"/>
    <circle cx="305" cy="218" r="8" fill="var(--brand-blue)"/>
    <text x="318" y="227" font-family="Open Sans, Arial, sans-serif" font-weight="600" font-size="24" fill="#6d6e70">Halvorn</text>
  </svg>

</body>
</html>
```